B2B telecom company need web design

We need a web design for our corporate web site. The company exists since almost 10 years.
This is a DESIGN contest, you're expected to provide design only, NOT the whole website. The winner will have to provide the HTML template (with Lorem Ipsum content) and the CSS files of his design.
Our initial product is SMS peering in P2P (you send a SMS to a friend in a foreign country, great chance that your operator route your SMS to us that we route to the recipient). We're launching a bulk SMS service (marketing and application to SMS).
Target is mostly corporate, usually big corporate (operators, contents providers...) where use of SMS is part of the main business.
The web site is composed of 1 landing page and 7 content pages (plan is given for your information, all content page are using the same template and the same design, you do NOT need to make one design per page) :
* About US
Company Profile
They trust us
The Volnor Team
Partners
Contact us
* Solution
P2P SMS
A2P SMS
You only need to submit the landing page and a template page for the content (with h1, h2, h3 and h4).
Design must be based on our new logo (see attached file).
Our current web site http://www.volnor-example.com
The winner of the contest will have to provide state of the art HTML template and CSS files of his design. Photo used shall be downloaded from Pixelbrook (provide the ID of the picture that we purchase file).
Target Market(s)
Telecom operator. SMS Peering hubs. Bulk SMS.
Industry/Entity Type
It Company
Number of Pages Required
2 page

```html
<!DOCTYPE html>
<html lang="en">
<head>
<meta charset="utf-8">
<title>Volnor</title>
<link href="https://fonts.googleapis.com/css2?family=Roboto:wght@300;400;500;700&display=swap" rel="stylesheet">
<style>
:root{
  --green:#8cc43f;
  --ink:#2b2b2b;
  --text:#6b6b6b;
  --nav:#1e1e1e;
  --grey:#efefef;
  --black:#111;
  --footer:#242424;
  --white:#fff;
}
*{box-sizing:border-box;margin:0;padding:0}
html,body{width:1200px;height:4602px;overflow:hidden}
body{font-family:"Roboto",Arial,sans-serif;color:var(--text);background:var(--white);font-size:13px;line-height:1.6}
section,header,footer{position:relative;width:1200px;overflow:hidden}
.title{font-size:36px;font-weight:500;letter-spacing:5px;color:var(--ink);text-align:center;text-transform:uppercase}
.rule{width:60px;height:2px;background:var(--green);margin:14px auto 0}
.lead{width:820px;margin:0 auto;text-align:center;font-size:13px;color:#555}
.btn{display:inline-block;background:var(--green);color:var(--white);font-size:12px;font-weight:700;text-transform:uppercase;padding:6px 16px;letter-spacing:1px}

/* nav */
.nav{height:64px;background:var(--nav);display:flex;align-items:center;justify-content:space-between;padding-left:96px}
.brand{color:var(--white);font-size:26px;font-weight:500;letter-spacing:1px}
.menu{display:flex;height:64px;margin-right:96px}
.menu a{display:flex;align-items:center;padding:0 20px;color:var(--white);font-size:12px;font-weight:700;text-decoration:none}
.menu a.active{background:var(--green)}

/* hero */
.hero{height:442px;background:linear-gradient(180deg,#cfe0b8,#dfeacf 70%,#e8f0dc)}
.hero .pattern{position:absolute;inset:0}
.hero .name{position:absolute;top:150px;width:100%;text-align:center;color:#3a3a3a;font-size:60px;font-weight:500;letter-spacing:2px}
.hero .tag{position:absolute;top:242px;width:100%;text-align:center;color:#5f7a45;font-size:14px;letter-spacing:2px}
.hero .ctas{position:absolute;top:296px;width:100%;text-align:center}
.hero .ctas .btn{margin:0 6px}
.arrow{position:absolute;top:240px;width:88px;height:90px;background:rgba(120,130,110,.35);display:flex;align-items:center;justify-content:center}
.arrow.l{left:0}.arrow.r{right:0}

/* about */
.about{height:620px;padding-top:78px}
.about .lead{margin-top:34px}
.cards{display:flex;justify-content:center;gap:36px;margin-top:40px}
.card{width:320px;text-align:center}
.card .photo{height:160px;width:100%}
.card h3{font-size:17px;font-weight:500;color:var(--ink);margin-top:14px}
.card p{font-size:12px;margin:10px 20px 0}

/* advantages */
.adv{height:619px;background:radial-gradient(ellipse at 50% 40%,#e9f0de,#d6e3c4 70%);padding-top:86px}
.adv .lead{margin-top:30px}
.grid2{display:grid;grid-template-columns:420px 420px;column-gap:80px;justify-content:center;margin-top:44px;row-gap:30px}
.item{display:flex;gap:18px}
.item .pic{flex:none;width:66px;height:66px;border-radius:50%}
.item h4{font-size:17px;font-weight:500;color:var(--ink)}
.item h4.hl{color:#5b8cc4}
.item p{font-size:12px;margin-top:4px}

/* services */
.services{height:662px;padding-top:88px}
.services .lead{margin-top:32px}
.services .grid2{row-gap:28px;margin-top:50px}
.ico{flex:none;width:46px;height:46px;border:2px solid var(--green);border-radius:50%;display:flex;align-items:center;justify-content:center}

/* solutions */
.solutions{height:407px;background:radial-gradient(ellipse at 50% 40%,#dce7cd,#c9d9b3 75%);padding-top:70px}
.solutions .title{color:var(--white)}
.sol-row{display:flex;justify-content:center;gap:40px;margin-top:44px}
.sol{width:300px;display:flex;gap:16px}
.sol .ico{background:rgba(255,255,255,.3)}
.sol h4{font-size:16px;font-weight:500;color:var(--ink)}
.sol p{font-size:12px;line-height:1.5;color:#4f5a44;margin-top:4px}

/* trust */
.trust{height:779px;background:var(--grey);padding-top:190px}
.trust .lead{margin-top:30px}
.quotes{display:grid;grid-template-columns:440px 440px;column-gap:80px;row-gap:60px;justify-content:center;margin-top:54px}
.quote{display:flex;gap:22px}
.quote .face{flex:none;width:100px;height:100px;border-radius:50%}
.quote p{font-size:12px;font-style:italic;margin-top:8px}
.quote .who{font-size:13px;font-weight:700;color:var(--ink);margin-top:10px;font-style:normal}

/* partners */
.partners{height:195px;background:var(--black);display:flex;justify-content:space-around;align-items:center;padding:0 90px}
.partner{display:flex;align-items:center;gap:8px;color:var(--white);font-size:22px;font-weight:700}
.partner .dot{width:22px;height:22px;border-radius:50%;background:var(--white)}

/* contact */
.contact{height:637px;background:radial-gradient(ellipse at 50% 30%,#e3ebd8,#c8d7b4 80%);padding-top:100px}
.contact .title{color:var(--white)}
.contact .lead{margin-top:28px;color:#4f5a44}
.cwrap{display:flex;justify-content:center;gap:120px;margin-top:42px}
.form{width:470px;display:flex;flex-direction:column;gap:14px}
.field{height:34px;border:1px solid rgba(255,255,255,.9);background:rgba(255,255,255,.15)}
.field.area{height:92px}
.form .btn{align-self:flex-start;margin-top:10px}
.info{width:420px;display:flex;flex-direction:column;gap:14px}
.info .row{display:flex;align-items:center;height:42px;border:1px solid rgba(255,255,255,.9);background:rgba(255,255,255,.15)}
.info .pin{width:42px;height:42px;background:var(--green);display:flex;align-items:center;justify-content:center;flex:none}
.info span{padding-left:14px;font-size:13px;color:#3f4a36}

/* footer */
.footer{height:177px;background:var(--footer);display:flex;align-items:center;justify-content:center;color:#cfcfcf;font-size:11px}
.totop{position:absolute;right:14px;width:36px;height:36px;border-radius:50%;background:#888;display:flex;align-items:center;justify-content:center}
</style>
</head>
<body>

<svg width="0" height="0" style="position:absolute"><defs><path id="s" d="M7 0l2 5h5l-4 3 2 5-5-3-5 3 2-5-4-3h5z"/></defs></svg>

<header class="nav">
  <div class="brand">Volnor</div>
  <nav class="menu">
    <a class="active" href="#">HOME</a>
    <a href="#">ABOUT US ▾</a>
    <a href="#">SOLUTION</a>
  </nav>
</header>

<section class="hero">
  <div class="pattern" role="img" aria-label="Faint world map with green network lines and nodes"></div>
  <div class="name">Volnor</div>
  <div class="tag">Messaging that gets things done</div>
  <div class="ctas"><span class="btn">About us</span><span class="btn">Solution</span></div>
  <div class="arrow l"><svg width="16" height="26" viewBox="0 0 16 26"><path d="M13 2L3 13l10 11" fill="none" stroke="#fff" stroke-width="3"/></svg></div>
  <div class="arrow r"><svg width="16" height="26" viewBox="0 0 16 26"><path d="M3 2l10 11L3 24" fill="none" stroke="#fff" stroke-width="3"/></svg></div>
</section>

<section class="about">
  <h2 class="title">We are Volnor</h2>
  <div class="rule"></div>
  <p class="lead">Volnor Mobile Exchange is the combination of world-class enterprise solutions and an unrivalled global data network, creating one of the global leaders in mobile enterprise software and services. The result for our customers is unlimited potential.</p>
  <div class="cards">
    <div class="card">
      <div class="photo" role="img" aria-label="Photo of hands holding a mobile phone" style="background:linear-gradient(135deg,#3a3a3a,#9a9a9a)"></div>
      <h3>Operator Services</h3>
      <p>Volnor Mobile Exchange offers operators comprehensive services to facilitate the delivery of mobile data and content.</p>
    </div>
    <div class="card">
      <div class="photo" role="img" aria-label="Photo of a hand touching a glowing message icon" style="background:linear-gradient(135deg,#1d1d1d,#5b5b5b)"></div>
      <h3>Brand &amp; Content Services</h3>
      <p>Volnor Mobile Exchange offers operators comprehensive services to facilitate the delivery of mobile data and content.</p>
    </div>
    <div class="card">
      <div class="photo" role="img" aria-label="Photo of a business team in a meeting" style="background:linear-gradient(135deg,#8a8a80,#d8d6cc)"></div>
      <h3>Enterprise Services</h3>
      <p>Volnor Mobile Exchange offers operators comprehensive services to facilitate the delivery of mobile data and content.</p>
    </div>
  </div>
</section>

<section class="adv">
  <h2 class="title">Advantages</h2>
  <div class="rule"></div>
  <p class="lead">Volnor Mobile Exchange leads the world in the delivery, billing and settlement of mobile messaging services. Volnor Mobile Exchange's global connectivity and network reliability inspire confidence that messages get delivered successfully, and that related revenue is processed quickly.</p>
  <div class="grid2">
    <div class="item"><div class="pic" role="img" aria-label="Round photo of a glowing globe" style="background:radial-gradient(circle,#4a6f8a,#0f1a24)"></div><div><h4>Global Reach</h4><p>Volnor Mobile Exchange &amp; Partners delivers any message to any handset, anytime, anywhere. With reach to more than 700 global operators, we are the partner of choice to reliably deliver, track and settle the world's mobile messages.</p></div></div>
    <div class="item"><div class="pic" role="img" aria-label="Round photo of server infrastructure" style="background:radial-gradient(circle,#5e7ea0,#141d28)"></div><div><h4 class="hl">Superior Infrastructure</h4><p>The Volnor Exchange network provides an operator-grade, high-volume delivery infrastructure that is fault-tolerant and scalable to meet even the highest standards.</p></div></div>
    <div class="item"><div class="pic" role="img" aria-label="Round photo of a reporting dashboard" style="background:radial-gradient(circle,#6a8fb0,#1b2735)"></div><div><h4>Comprehensive Reporting</h4><p>Using our comprehensive, Web-based reporting tools, customers track and analyze traffic trends, such as message origination and termination by operator, peak traffic times, active rate monitoring, hourly/daily/weekly/monthly views, global traffic and country error reporting.</p></div></div>
    <div class="item"><div class="pic" role="img" aria-label="Round photo of coins and clearing charts" style="background:radial-gradient(circle,#c9a24a,#3a2a10)"></div><div><h4>Integrated Clearing + Settlement</h4><p>With a variety of billing mechanisms that ensure your revenue gets rapidly delivered in currencies worldwide, Volnor Exchange enables companies to distribute messages and content while simultaneously generating revenue via a wide range of mobile messaging solutions.</p></div></div>
  </div>
</section>

<section class="services">
  <h2 class="title">Our Services</h2>
  <div class="rule"></div>
  <p class="lead">Volnor Mobile Exchange offers operators comprehensive services to facilitate the delivery of mobile data and content. Our global interoperability experience and capabilities are unrivalled. Providing operators with expanded reach both to other networks and to greater subscriber content via only as many operators select Volnor Mobile Exchange as the vendor of choice.</p>
  <div class="grid2">
    <div class="item"><div class="ico"><svg width="20" height="20" viewBox="0 0 20 20"><path d="M2 9h4v9H2zM7 9l4-7c2 0 2 2 1 5h5l-2 11H7z" fill="#8cc43f"/></svg></div><div><h4>Operator-grade Reliability</h4><p>Sed ut perspiciatis unde omnis iste natus error sit voluptatem accusantium doloremque laudantium totam rem.</p></div></div>
    <div class="item"><div class="ico"><svg width="20" height="20" viewBox="0 0 20 20"><rect x="3" y="6" width="14" height="8" rx="4" fill="#8cc43f"/></svg></div><div><h4>High-availability &amp; Fault-tolerance</h4><p>High-availability and fault-tolerance that facilitates the seamless transmission of all types of messaging.</p></div></div>
    <div class="item"><div class="ico"><svg width="20" height="20" viewBox="0 0 20 20"><rect x="2" y="4" width="16" height="12" fill="none" stroke="#8cc43f" stroke-width="2"/><path d="M2 4l8 7 8-7" fill="none" stroke="#8cc43f" stroke-width="2"/></svg></div><div><h4>Message Delivery</h4><p>Message delivery across all mobile operators around the world.</p></div></div>
    <div class="item"><div class="ico"><svg width="20" height="20" viewBox="0 0 20 20"><circle cx="5" cy="10" r="3" fill="#8cc43f"/><circle cx="15" cy="4" r="3" fill="#8cc43f"/><circle cx="15" cy="16" r="3" fill="#8cc43f"/><path d="M5 10l10-6M5 10l10 6" stroke="#8cc43f" stroke-width="2"/></svg></div><div><h4>Sophisticated Infrastructure</h4><p>A sophisticated infrastructure that features transcoding capabilities that traverse networks and handsets without degrading message quality.</p></div></div>
    <div class="item"><div class="ico"><svg width="20" height="20" viewBox="0 0 20 20"><circle cx="10" cy="10" r="8" fill="none" stroke="#8cc43f" stroke-width="2"/><path d="M2 10h16M10 2c4 4 4 12 0 16M10 2c-4 4-4 12 0 16" fill="none" stroke="#8cc43f" stroke-width="1.5"/></svg></div><div><h4>Global Service</h4><p>Sed ut perspiciatis unde omnis iste natus error sit voluptatem accusantium doloremque laudantium totam rem.</p></div></div>
    <div class="item"><div class="ico"><svg width="20" height="20" viewBox="0 0 20 20"><circle cx="10" cy="6" r="4" fill="#8cc43f"/><path d="M2 19c0-5 4-7 8-7s8 2 8 7z" fill="#8cc43f"/></svg></div><div><h4>Customer Support</h4><p>Sed ut perspiciatis unde omnis iste natus error sit voluptatem accusantium doloremque laudantium totam rem.</p></div></div>
  </div>
</section>

<section class="solutions">
  <h2 class="title">Solutions</h2>
  <div class="rule" style="background:#fff"></div>
  <div class="sol-row">
    <div class="sol"><div class="ico"><svg width="20" height="20" viewBox="0 0 20 20"><path d="M3 10l5 5 9-10" fill="none" stroke="#8cc43f" stroke-width="3"/></svg></div><div><h4>365 Interoperability Services</h4><p>Connect your customers, 365 days a year. Global operators – Volnor &amp; Partners are the leader in messaging interoperability using SS7 and SIGTRAN.</p></div></div>
    <div class="sol"><div class="ico"><svg width="20" height="20" viewBox="0 0 20 20"><path d="M3 10l5 5 9-10" fill="none" stroke="#8cc43f" stroke-width="3"/></svg></div><div><h4>Reporting + Statistics</h4><p>Using our Web-based reporting tools, customers track and analyze traffic trends such as origination and termination by operator, peak traffic times, active rate monitoring, daily and monthly views, and error reporting.</p></div></div>
    <div class="sol"><div class="ico"><svg width="20" height="20" viewBox="0 0 20 20"><path d="M3 10l5 5 9-10" fill="none" stroke="#8cc43f" stroke-width="3"/></svg></div><div><h4>Integrated Clearing + Settlement</h4><p>With a variety of billing mechanisms that ensure your revenue gets rapidly delivered in currencies worldwide, Volnor Exchange enables companies to distribute messages and content while generating revenue.</p></div></div>
  </div>
</section>

<section class="trust">
  <h2 class="title">They Trust Us</h2>
  <div class="rule"></div>
  <p class="lead">Lorem ipsum dolor sit amet, consectetur adipisicing elit, sed do eiusmod tempor incididunt ut labore et dolore magna aliqua. Ut enim ad minim veniam, quis nostrud exercitation ullamco laboris nisi ut aliquip ex ea commodo consequat.</p>
  <div class="quotes">
    <div class="quote"><div class="face" role="img" aria-label="Round portrait photo of a client" style="background:radial-gradient(circle,#c9b5a0,#7e6a58)"></div><div>
      <svg width="90" height="14" viewBox="0 0 90 14"><g fill="#8cc43f"><use href="#s"/><use href="#s" x="18"/><use href="#s" x="36"/><use href="#s" x="54"/><use href="#s" x="72"/></g></svg>
      <p>"Lorem ipsum dolor sit amet, consectetur adipisicing elit, sed do eiusmod tempor incididunt ut labore et dolore magna aliqua."</p><p class="who">Daniel Forde</p></div></div>
    <div class="quote"><div class="face" role="img" aria-label="Round portrait photo of a client" style="background:radial-gradient(circle,#d6b39a,#7a4f3c)"></div><div>
      <svg width="90" height="14" viewBox="0 0 90 14"><g fill="#8cc43f"><use href="#s"/><use href="#s" x="18"/><use href="#s" x="36"/><use href="#s" x="54"/><use href="#s" x="72"/></g></svg>
      <p>"Lorem ipsum dolor sit amet, consectetur adipisicing elit, sed do eiusmod tempor incididunt ut labore et dolore magna aliqua."</p><p class="who">Laura Whitcombe</p></div></div>
    <div class="quote"><div class="face" role="img" aria-label="Round portrait photo of a client" style="background:radial-gradient(circle,#e0c6ad,#8d6e56)"></div><div>
      <svg width="90" height="14" viewBox="0 0 90 14"><g fill="#8cc43f"><use href="#s"/><use href="#s" x="18"/><use href="#s" x="36"/><use href="#s" x="54"/></g><use href="#s" x="72" fill="#c8c8c8"/></svg>
      <p>"Lorem ipsum dolor sit amet, consectetur adipisicing elit, sed do eiusmod tempor incididunt ut labore et dolore magna aliqua. Ut enim ad minim veniam, quis nostrud exercitation."</p><p class="who">Nina Carrow</p></div></div>
    <div class="quote"><div class="face" role="img" aria-label="Round portrait photo of a client" style="background:radial-gradient(circle,#cdb8a4,#5f5148)"></div><div>
      <svg width="90" height="14" viewBox="0 0 90 14"><g fill="#8cc43f"><use href="#s"/><use href="#s" x="18"/><use href="#s" x="36"/></g><g fill="#c8c8c8"><use href="#s" x="54"/><use href="#s" x="72"/></g></svg>
      <p>"Lorem ipsum dolor sit amet, consectetur adipisicing elit, sed do eiusmod tempor incididunt ut labore et dolore magna aliqua. Ut enim ad minim veniam, quis nostrud exercitation."</p><p class="who">Peter Lindqvist</p></div></div>
  </div>
</section>

<section class="partners">
  <div class="partner"><span class="dot"></span>Brookline</div>
  <div class="partner"><span class="dot"></span>Halvex</div>
  <div class="partner">Solvane</div>
  <div class="partner">Meridel</div>
  <div class="partner">Corvanta</div>
  <div class="partner">Tablefare</div>
</section>

<section class="contact">
  <h2 class="title">Contact Us</h2>
  <div class="rule" style="background:#fff"></div>
  <p class="lead">Lorem ipsum dolor sit amet, consectetur adipisicing elit, sed do eiusmod tempor incididunt ut labore et dolore magna aliqua. Ut enim ad minim veniam, quis nostrud exercitation ullamco laboris nisi ut aliquip ex ea commodo consequat.</p>
  <div class="cwrap">
    <div class="form">
      <div class="field"></div>
      <div class="field"></div>
      <div class="field"></div>
      <div class="field area"></div>
      <span class="btn">Send Message</span>
    </div>
    <div class="info">
      <div class="row"><div class="pin"><svg width="14" height="18" viewBox="0 0 14 18"><path d="M7 0a7 7 0 00-7 7c0 5 7 11 7 11s7-6 7-11a7 7 0 00-7-7zm0 10a3 3 0 110-6 3 3 0 010 6z" fill="#fff"/></svg></div><span>Rue des Tilleuls 14, 1200 Lakeport</span></div>
      <div class="row"><div class="pin"><svg width="16" height="16" viewBox="0 0 16 16"><path d="M3 1l3 3-2 2c1 2 3 4 6 6l2-2 3 3-2 2C7 15 1 9 1 3z" fill="#fff"/></svg></div><span>+00 (0) 555 01 23</span></div>
      <div class="row"><div class="pin"><svg width="16" height="12" viewBox="0 0 16 12"><rect x="1" y="1" width="14" height="10" fill="none" stroke="#fff" stroke-width="2"/><path d="M1 1l7 6 7-6" fill="none" stroke="#fff" stroke-width="2"/></svg></div><span>info@volnor-example.com</span></div>
      <div class="row"><div class="pin"><svg width="16" height="16" viewBox="0 0 16 16"><circle cx="8" cy="8" r="7" fill="none" stroke="#fff" stroke-width="2"/><circle cx="8" cy="8" r="2" fill="#fff"/></svg></div><span>volnor-mobile</span></div>
    </div>
  </div>
  <div class="totop" style="bottom:40px"><svg width="12" height="8" viewBox="0 0 12 8"><path d="M1 7l5-5 5 5" fill="none" stroke="#fff" stroke-width="2"/></svg></div>
</section>

<footer class="footer">
  Copyright © 2015 Volnor
  <div class="totop" style="bottom:40px"><svg width="12" height="8" viewBox="0 0 12 8"><path d="M1 7l5-5 5 5" fill="none" stroke="#fff" stroke-width="2"/></svg></div>
</footer>

</body>
</html>
```